Profesional personal website needs design and business card

I need a business card with my professional name as a logo "Marlo Vitality" for my business. I am a Wellness Coach, consultant and trainer. So it should be professional, wellness oriented and modern.

Target Market(s)

Private clients, governments, corporations. Luxury and high market.

Industry/Entity Type

Health And Wellness

Contact Information for Business Card

Marlo Vitality should be the logo

Colors

Designer to choose colors to be used in the design.

Requirements
Must have
• Marlo Vitality
• Name: Tomás Arribal
• Wellness Coach, Consultant & Trainer.
• Website: www.marlovitality.example
• Phone:
• Spain (+34) 612 480 397
• (USA) +1 (555) 318 2046
Nice to have
• The most important is the design of "Marlo Vitality", as this is going to be my personal brand logo. It should be professional, wellness, high end and actual.
Should not have
• no golds, no baroque style..

```html
<!DOCTYPE html>
<html lang="en">
<head>
<meta charset="utf-8">
<title>Marlo Vitality – Business Card</title>
<link rel="stylesheet" href="https://fonts.googleapis.com/css2?family=Montserrat:wght@500;600&family=Roboto:wght@400&display=swap">
<style>
  :root {
    --backdrop: #d9d9d6;
    --card-white: #ffffff;
    --brand-green: #3f8233;
    --brand-green-dark: #336f29;
    --map-dot: rgba(255, 255, 255, 0.10);
    --ink: #4a4a4a;
    --ring-grey: #8c8c8c;
  }
  * { box-sizing: border-box; margin: 0; padding: 0; }
  html, body {
    width: 1200px; height: 801px; overflow: hidden;
    background: var(--backdrop);
  }
  .stage {
    position: relative; width: 1200px; height: 801px;
    display: flex; align-items: center; justify-content: center; gap: 50px;
  }
  .card {
    position: relative; width: 540px; height: 309px;
    box-shadow: 0 6px 18px rgba(0,0,0,0.18);
    overflow: hidden;
  }
  /* Front */
  .card--front { background: var(--card-white); }
  .front-brand {
    position: absolute; top: 58px; right: 60px;
    display: flex; align-items: center; gap: 14px;
  }
  .brand-dot {
    width: 44px; height: 44px; border-radius: 50%;
    background: var(--brand-green);
    box-shadow: 0 0 0 3px var(--card-white), 0 0 0 5px var(--ring-grey);
  }
  .brand-name {
    font-family: "Montserrat", sans-serif; font-weight: 600;
    text-transform: uppercase; letter-spacing: 0.04em;
    font-size: 24px; color: var(--brand-green);
  }
  .front-details { position: absolute; left: 40px; bottom: 34px; }
  .person-name {
    font-family: "Montserrat", sans-serif; font-weight: 600;
    text-transform: uppercase; font-size: 23px; color: var(--brand-green);
    letter-spacing: 0.02em; line-height: 1.1;
  }
  .person-role {
    font-family: "Roboto", sans-serif; font-size: 12.5px; color: var(--ink);
    margin: 3px 0 10px; letter-spacing: 0.02em;
  }
  .contact-list { list-style: none; font-family: "Roboto", sans-serif; font-size: 13.5px; color: var(--ink); }
  .contact-list li { line-height: 1.5; letter-spacing: 0.02em; }
  .contact-label { color: var(--brand-green); font-family: "Montserrat", sans-serif; font-weight: 600; display: inline-block; width: 26px; }
  /* Back */
  .card--back { background: linear-gradient(160deg, var(--brand-green) 0%, var(--brand-green) 60%, var(--brand-green-dark) 100%); }
  .map-area {
    position: absolute; left: 40px; top: 40px; right: 40px; bottom: 30px;
    background: radial-gradient(ellipse at 50% 50%, var(--map-dot) 0%, rgba(255,255,255,0.05) 60%, transparent 80%);
  }
  .back-brand {
    position: absolute; inset: 0;
    display: flex; flex-direction: column; align-items: center; justify-content: center; gap: 18px;
  }
  .back-ring {
    width: 92px; height: 92px; border-radius: 50%;
    border: 4px solid var(--card-white);
    display: flex; align-items: center; justify-content: center;
  }
  .back-ring span { width: 70px; height: 70px; border-radius: 50%; background: var(--card-white); }
  .back-name {
    font-family: "Montserrat", sans-serif; font-weight: 600;
    text-transform: uppercase; letter-spacing: 0.04em;
    font-size: 36px; color: var(--card-white);
  }
</style>
</head>
<body>
<main class="stage">
  <section class="card card--front" aria-label="Business card front">
    <div class="front-brand">
      <span class="brand-dot"></span>
      <span class="brand-name">Marlo Vitality</span>
    </div>
    <div class="front-details">
      <h1 class="person-name">Tomás Arribal</h1>
      <p class="person-role">Wellness Coach, Consultant &amp; Trainer</p>
      <ul class="contact-list">
        <li><span class="contact-label">P :</span>(+34) 612 480 397 (Spain)</li>
        <li><span class="contact-label">P :</span>+1 (555) 318 2046 (USA)</li>
        <li><span class="contact-label">E :</span>info@marlovitality.example</li>
        <li><span class="contact-label">W :</span>www.marlovitality.example</li>
      </ul>
    </div>
  </section>

  <section class="card card--back" aria-label="Business card back">
    <div class="map-area" role="img" aria-label="Faint dotted world map pattern"></div>
    <div class="back-brand">
      <div class="back-ring"><span></span></div>
      <p class="back-name">Marlo Vitality</p>
    </div>
  </section>
</main>
</body>
</html>
```